Cedar Lantern Letterhead

I just need letterhead for my integrative psychiatry business. I'm going to use this to do mailings to other doctors, as well as send letters to patients. Thank you

Business

```html
<!DOCTYPE html>
<html lang="en">
<head>
<meta charset="utf-8">
<title>Cedar Lantern Letterhead</title>
<link rel="stylesheet" href="https://fonts.googleapis.com/css2?family=Source+Sans+3:wght@400;600&display=swap">
<style>
  :root {
    --backdrop: #c4c5c7;
    --paper: #ebeced;
    --leaf-green: #2f6e33;
    --bark-brown: #5a2d14;
    --ink-green: #2f6e33;
  }
  * { margin: 0; padding: 0; box-sizing: border-box; }
  html, body {
    width: 1200px;
    height: 848px;
    overflow: hidden;
    background: var(--backdrop);
    font-family: "Source Sans 3", "Myriad Pro", Arial, sans-serif;
  }
  .letterhead {
    position: absolute;
    left: 350px;
    top: 72px;
    width: 498px;
    height: 703px;
    background: var(--paper);
  }
  .header-swoosh {
    position: absolute;
    left: 0;
    top: 0;
    width: 498px;
    height: 80px;
  }
  .leaf-sprig {
    position: absolute;
    left: 63px;
    top: 27px;
    width: 54px;
    height: 24px;
    border-radius: 50% 50% 4px 4px;
    background: var(--leaf-green);
  }
  .brand {
    position: absolute;
    right: 22px;
    top: 76px;
    display: flex;
    align-items: center;
    gap: 6px;
    color: var(--leaf-green);
    font-weight: 600;
    font-size: 15px;
    letter-spacing: 0.2px;
  }
  .brand-dot {
    width: 10px;
    height: 10px;
    border-radius: 50%;
    background: var(--leaf-green);
  }
  .contact-block {
    position: absolute;
    left: 22px;
    top: 632px;
    font-size: 8px;
    line-height: 7.6px;
    color: var(--ink-green);
    list-style: none;
  }
  .credentials {
    position: absolute;
    right: 18px;
    top: 663px;
    font-size: 8px;
    line-height: 7.6px;
    color: var(--ink-green);
    text-align: right;
    list-style: none;
  }
</style>
</head>
<body>
  <main class="letterhead">
    <svg class="header-swoosh" viewBox="0 0 498 80" aria-hidden="true">
      <path d="M2 34 C40 50 70 56 110 53 C200 46 280 26 370 24 C420 23 460 26 495 30"
            fill="none" stroke="var(--leaf-green)" stroke-width="3" stroke-linecap="round"/>
      <path d="M2 40 C30 62 70 72 120 68 C210 60 290 40 380 37 C430 36 465 38 495 42"
            fill="none" stroke="var(--bark-brown)" stroke-width="3.5" stroke-linecap="round"/>
    </svg>
    <div class="leaf-sprig" role="img" aria-label="Small sprig of three green leaves resting on the curve"></div>

    <div class="brand">
      <span class="brand-dot"></span>
      <span class="brand-name">Cedar Lantern</span>
    </div>

    <ul class="contact-block">
      <li>555-014-2286</li>
      <li>555-014-2287</li>
      <li>2180 Alder Bend Road</li>
      <li>Suite 210</li>
      <li>Maple Ford, CA 95999</li>
      <li>www.cedarlanternhealth.com</li>
    </ul>

    <ul class="credentials">
      <li>Diplomat, National Board of Mind and Brain Medicine</li>
      <li>Diplomat, National Board of Whole-Person Medicine</li>
    </ul>
  </main>
</body>
</html>
```